Norvane Builders Business Card

Modern and Professional Business Card for a Med size construction/development company.

See the samples below for the design I like … but I need ideas for incorporating the red company logo while still keeping the clean look of the card samples that are attached.

Logo and tag line on the back … info on the front.

Tagline: Quality Starts from the Ground Up

Target Market(s)

Med-Large General Contractors

Contact Information for Business Card

Norvane Builders Limited
42 Brenton Street
Elk Harbour, NL
B3K 7T2

t: 709-555-0147
f: 709-555-0192
w: www.norvanebuilders-example.com

Font styles to use
Sans Serif

Colors
fbee3e

Requirements
Must have
• I like the black and yellow designs of the attached samples …. but I'm not sure how to incorporate the red Norvane Builders logo into that design??
Nice to have
• Construction safety strips

```html
<!DOCTYPE html>
<html lang="en">
<head>
<meta charset="utf-8">
<title>Norvane Builders Business Card</title>
<link href="https://fonts.googleapis.com/css2?family=Arvo:wght@400;700&display=swap" rel="stylesheet">
<style>
  :root {
    --backdrop: #3a3a3a;
    --card-black: #0d0d0d;
    --safety-yellow: #fbee3e;
    --safety-yellow-dim: #d9cd3a;
    --brand-red: #e3202a;
    --ink: #1a1a1a;
  }
  html, body {
    margin: 0;
    width: 1200px;
    height: 900px;
    overflow: hidden;
    background: var(--backdrop);
    font-family: "Arvo", Georgia, serif;
  }
  .card {
    position: absolute;
    left: 250px;
    width: 700px;
    height: 400px;
    background: var(--card-black);
    overflow: hidden;
    box-shadow: 0 10px 30px rgba(0,0,0,.45);
  }
  .card--back { top: 40px; }
  .card--front { top: 470px; }

  .safety-strip {
    position: absolute;
    width: 22px;
    background: repeating-linear-gradient(
      to bottom,
      var(--safety-yellow) 0 40px,
      var(--safety-yellow-dim) 40px 80px
    );
  }
  .card--back .safety-strip--left { left: 26px; top: 0; height: 240px; }
  .card--back .safety-strip--right { right: 26px; top: 130px; height: 270px; }
  .card--front .safety-strip--left { left: 22px; top: 30px; height: 340px; }

  .wordmark {
    position: absolute;
    color: var(--brand-red);
    font-weight: 700;
    text-align: center;
    line-height: 1;
    text-transform: uppercase;
  }
  .wordmark__name { display: block; font-size: 56px; letter-spacing: 1px; }
  .wordmark__sub { display: block; font-size: 20px; letter-spacing: 3px; margin-top: 10px; }
  .card--back .wordmark { left: 0; right: 0; top: 120px; }
  .card--front .wordmark { left: 60px; width: 280px; top: 150px; }
  .card--front .wordmark__name { font-size: 44px; }
  .card--front .wordmark__sub { font-size: 15px; letter-spacing: 2px; }

  .tagline {
    position: absolute;
    left: 0; right: 0;
    top: 285px;
    margin: 0;
    text-align: center;
    color: var(--safety-yellow);
    font-size: 18px;
    letter-spacing: 1px;
    text-transform: uppercase;
  }

  .divider {
    position: absolute;
    left: 352px; top: 50px;
    width: 5px; height: 300px;
    background: var(--brand-red);
  }
  .info-panel {
    position: absolute;
    left: 368px; top: 58px;
    width: 332px; height: 312px;
    background: var(--safety-yellow);
    color: var(--ink);
    box-sizing: border-box;
    padding: 32px 14px 0 30px;
  }
  .person__name { margin: 0; font-size: 24px; font-weight: 400; letter-spacing: 1px; line-height: 1.2; }
  .person__role { margin: 0 0 18px; font-size: 15px; color: var(--brand-red); }
  .contact { list-style: none; margin: 0; padding: 0; font-size: 17px; }
  .contact__item { display: flex; align-items: flex-start; margin-bottom: 10px; }
  .contact__icon {
    flex: none;
    width: 28px; height: 28px;
    margin-right: 12px;
    border-radius: 4px;
    background: var(--brand-red);
    display: flex; align-items: center; justify-content: center;
  }
  .contact__text { padding-top: 3px; line-height: 1.35; white-space: nowrap; }
  .contact__text--web { font-size: 12.5px; padding-top: 6px; }
</style>
</head>
<body>

<section class="card card--back" aria-label="Card back">
  <div class="safety-strip safety-strip--left"></div>
  <div class="safety-strip safety-strip--right"></div>
  <div class="wordmark">
    <span class="wordmark__name">Norvane</span>
    <span class="wordmark__sub">Builders Limited</span>
  </div>
  <p class="tagline">Quality Starts from the Ground Up</p>
</section>

<section class="card card--front" aria-label="Card front">
  <div class="safety-strip safety-strip--left"></div>
  <div class="wordmark">
    <span class="wordmark__name">Norvane</span>
    <span class="wordmark__sub">Builders Limited</span>
  </div>
  <div class="divider"></div>
  <div class="info-panel">
    <h1 class="person__name">JOHN DOE</h1>
    <p class="person__role">Contractor</p>
    <ul class="contact">
      <li class="contact__item">
        <span class="contact__icon">
          <svg width="18" height="18" viewBox="0 0 24 24" fill="#fff"><path d="M6.6 10.8a15 15 0 0 0 6.6 6.6l2.2-2.2c.3-.3.7-.4 1-.2 1.1.4 2.3.6 3.6.6.6 0 1 .4 1 1V20c0 .6-.4 1-1 1A17 17 0 0 1 3 4c0-.6.4-1 1-1h3.5c.6 0 1 .4 1 1 0 1.3.2 2.5.6 3.6.1.3 0 .7-.2 1z"/></svg>
        </span>
        <span class="contact__text">709 - 555 - 0147</span>
      </li>
      <li class="contact__item">
        <span class="contact__icon">
          <svg width="18" height="18" viewBox="0 0 24 24" fill="#fff"><path d="M7 3h8l2 2v4H7z"/><rect x="3" y="10" width="18" height="11" rx="1.5"/><rect x="6" y="13" width="8" height="1.6" fill="#e3202a"/><rect x="6" y="16" width="8" height="1.6" fill="#e3202a"/></svg>
        </span>
        <span class="contact__text">709 - 555 - 0192</span>
      </li>
      <li class="contact__item">
        <span class="contact__icon">
          <svg width="18" height="18" viewBox="0 0 24 24" fill="none" stroke="#fff" stroke-width="2"><circle cx="12" cy="12" r="9"/><path d="M3 12h18M12 3c3 3 3 15 0 18M12 3c-3 3-3 15 0 18"/></svg>
        </span>
        <span class="contact__text contact__text--web">www.norvanebuilders-example.com</span>
      </li>
      <li class="contact__item">
        <span class="contact__icon">
          <svg width="18" height="18" viewBox="0 0 24 24" fill="#fff"><path d="M12 2a7 7 0 0 0-7 7c0 5 7 13 7 13s7-8 7-13a7 7 0 0 0-7-7zm0 9.5A2.5 2.5 0 1 1 12 6.5a2.5 2.5 0 0 1 0 5z"/></svg>
        </span>
        <span class="contact__text">42 Brenton Street<br>Elk Harbour, NL, B3K 7T2</span>
      </li>
    </ul>
  </div>
</section>

</body>
</html>
```